I own a small business whose primary function is Professional Fashion and Commercial Photography and has a secondary function of Talent Management of Models/Actors. I've used PrintaNova in the past to print my own design, but I'd like something a bit more topical, fresh and done by an artist instead of a photographer (me).

My company logo is included with a few selected horizontal (landscape) photos of some of my models--I'd like to use a single model photo as the background for the entire card, either in color or converted to black and white, at opacity enough to see the photo but not too much to obscure any text or the company logo, or use a photo as a share of the card (not the entire background), or use all the three models on the card in some manor... Our company colors are white, black, grey-silver and red.

Industry/Entity Type

Small Business

Contact Information for Business Card

Darnell Voskuijl, Owner
KLT Studios
PO Box 7316
Millbrook VT 05999-7316
(555) 014-2273
dan@kltstudios-example.com

```html
<!DOCTYPE html>
<html lang="en">
<head>
<meta charset="utf-8">
<title>KLT Studios – Business Card</title>
<link href="https://fonts.googleapis.com/css2?family=Arimo:wght@400;700&display=swap" rel="stylesheet">
<style>
  :root {
    --bg: #2b2b2d;
    --card-light: #dcdcdc;
    --ink: #1c1c1c;
    --ink-soft: #3a3a3a;
    --rule-grey: #6b6b6b;
    --brand-red: #d21f26;
    --white-veil: rgba(255,255,255,0.5);
  }
  * { box-sizing: border-box; margin: 0; padding: 0; }
  html, body { width: 1200px; height: 900px; overflow: hidden; }
  body {
    background: var(--bg);
    font-family: "Arimo", Arial, sans-serif;
    color: var(--ink);
    position: relative;
  }
  .card {
    position: absolute;
    left: 285px;
    width: 630px;
    height: 360px;
    overflow: hidden;
    box-shadow: 0 10px 30px rgba(0,0,0,0.5);
  }
  .card--front { top: 50px; }
  .card--back { top: 470px; background: var(--card-light); }

  /* Front */
  .model-strip { display: flex; height: 100%; }
  .model-photo { height: 100%; }
  .model-photo--skater {
    width: 38%;
    background:
      radial-gradient(ellipse 55% 35% at 50% 8%, #1e1e22 0%, rgba(30,30,34,0) 100%),
      radial-gradient(ellipse 45% 40% at 50% 50%, #c9a38a 0%, rgba(201,163,138,0) 100%),
      linear-gradient(180deg, #2c2b2e 0%, #6b5238 45%, #7c7b7e 100%);
  }
  .model-photo--red {
    width: 29%;
    background:
      radial-gradient(ellipse 45% 25% at 50% 28%, #c99a80 0%, rgba(201,154,128,0) 100%),
      radial-gradient(ellipse 60% 40% at 55% 70%, #e0402e 0%, rgba(224,64,46,0) 100%),
      linear-gradient(180deg, #b3171d 0%, #c42127 100%);
  }
  .model-photo--outdoor {
    width: 33%;
    background:
      radial-gradient(ellipse 50% 35% at 50% 35%, #dcb59c 0%, rgba(220,181,156,0) 100%),
      radial-gradient(ellipse 60% 25% at 50% 8%, #a9a7a3 0%, rgba(169,167,163,0) 100%),
      linear-gradient(180deg, #5e8c36 0%, #9da06a 30%, #c6343a 70%, #b8232b 100%);
  }
  .front-band {
    position: absolute; left: 0; right: 0; bottom: 0; height: 140px;
    background: var(--white-veil);
  }
  .front-brand { position: absolute; left: 30px; bottom: 48px; }

  /* Shared brand */
  .brand { display: flex; align-items: center; gap: 12px; position: relative; }
  .brand-mark { width: 24px; height: 24px; background: var(--brand-red); flex: none; }
  .brand-name { font-size: 36px; font-weight: 700; color: var(--ink); letter-spacing: 1px; white-space: nowrap; }
  .brand-rule {
    position: absolute; left: 36px; top: 50%; width: 380px; height: 2px;
    background: var(--brand-red); transform: translateY(22px);
  }
  .brand .brand-name { position: relative; z-index: 1; }

  /* Back */
  .back-photo {
    position: absolute; inset: 0;
    background:
      radial-gradient(ellipse 14% 22% at 72% 22%, #c4c4c4 0%, rgba(196,196,196,0) 100%),
      radial-gradient(ellipse 35% 45% at 70% 75%, #a6a6a6 0%, rgba(166,166,166,0) 100%),
      linear-gradient(90deg, #d4d4d4 0%, #cbcbcb 40%, #bdbdbd 70%, #cfcfcf 100%);
    opacity: 0.9;
  }
  .back-content { position: absolute; inset: 0; padding: 34px 0 0 46px; }
  .tagline { margin-top: 30px; font-size: 15px; font-weight: 700; color: var(--ink); letter-spacing: 0.2px; }
  .owner { margin: 34px 0 0 62px; }
  .owner-name { font-size: 17px; font-weight: 700; color: var(--ink-soft); }
  .owner-title { font-size: 16px; color: var(--ink-soft); margin-left: 112px; }
  .contact-list { list-style: none; margin-top: 46px; }
  .contact-item {
    display: flex; align-items: center; gap: 14px;
    font-size: 17px; color: var(--ink); height: 26px;
  }
  .contact-icon { width: 16px; height: 16px; fill: none; stroke: var(--ink-soft); stroke-width: 1.6; flex: none; }
  .contact-icon--pin { fill: var(--ink-soft); stroke: none; }
</style>
</head>
<body>

<section class="card card--front">
  <div class="model-strip">
    <div class="model-photo model-photo--skater" role="img" aria-label="Portrait of a young male model in a black cap"></div>
    <div class="model-photo model-photo--red" role="img" aria-label="Young male model in a red sleeveless shirt on a red backdrop"></div>
    <div class="model-photo model-photo--outdoor" role="img" aria-label="Young boy model in a red t-shirt outdoors with greenery"></div>
  </div>
  <div class="front-band"></div>
  <div class="front-brand brand">
    <span class="brand-mark"></span>
    <span class="brand-name">KLT Studios</span>
    <span class="brand-rule"></span>
  </div>
</section>

<section class="card card--back">
  <div class="back-photo" role="img" aria-label="Faded black-and-white photo of a young model in a plaid shirt"></div>
  <div class="back-content">
    <div class="brand">
      <span class="brand-mark"></span>
      <span class="brand-name">KLT Studios</span>
      <span class="brand-rule"></span>
    </div>
    <p class="tagline">Pro Fashion | Commercial Photography | Talent Management</p>
    <div class="owner">
      <p class="owner-name">Darnell Voskuijl,</p>
      <p class="owner-title">Owner</p>
    </div>
    <ul class="contact-list">
      <li class="contact-item">
        <svg class="contact-icon" viewBox="0 0 16 16"><circle cx="8" cy="8" r="7"/><path d="M5.5 4.5c0 3.5 2.5 6.5 5.5 7l1-1.6-1.8-1-0.9 0.8c-1-0.5-2-1.6-2.4-2.6l0.8-0.9-1-1.8z"/></svg>
        <span>(555) 014-2273</span>
      </li>
      <li class="contact-item">
        <svg class="contact-icon" viewBox="0 0 16 16"><rect x="1.5" y="3.5" width="13" height="9"/><path d="M1.5 3.5l6.5 5 6.5-5"/></svg>
        <span>dan@kltstudios-example.com</span>
      </li>
      <li class="contact-item">
        <svg class="contact-icon contact-icon--pin" viewBox="0 0 16 16"><path d="M8 1a4.5 4.5 0 0 0-4.5 4.5C3.5 9 8 15 8 15s4.5-6 4.5-9.5A4.5 4.5 0 0 0 8 1zm0 6.3a1.8 1.8 0 1 1 0-3.6 1.8 1.8 0 0 1 0 3.6z"/></svg>
        <span>PO Box 7316 Millbrook VT 05999</span>
      </li>
    </ul>
  </div>
</section>

</body>
</html>
```